A label for my commercially sold local honey. This is a LABEL not a logo

3 inches high
2 inches wide

Target Market(s)

Customers who like "local" honey

Logo Text

Wildflower Honey -- 100% Pure & Unfiltered -- Florida

Logo styles of interest
Wordmark Logo
Requirements
Must have
• Wildflower Honey -- 100% Pure & Unfiltered -- Florida

Florida should be dominant

3 inches high / 2 inches wide

```html
<!DOCTYPE html>
<html lang="en">
<head>
<meta charset="utf-8">
<title>Wildflower Honey Label</title>
<link href="https://fonts.googleapis.com/css2?family=Oswald:wght@600;700&family=Montserrat:wght@700;800&display=swap" rel="stylesheet">
<style>
  :root {
    --backdrop: #c9671c;
    --label-black: #121212;
    --honey-orange: #e08a1c;
    --honey-gold: #f7b733;
    --band-orange-dark: #b85f10;
    --paper: #f1f1f1;
    --floral-grey: #cfcfcf;
    --ink: #1c1c1c;
    --white: #ffffff;
  }
  * { margin: 0; padding: 0; box-sizing: border-box; }
  html, body {
    width: 1200px;
    height: 871px;
    overflow: hidden;
    background: var(--backdrop);
  }
  .canvas {
    position: relative;
    width: 1200px;
    height: 871px;
  }
  .label {
    position: absolute;
    left: 340px;
    top: 45px;
    width: 520px;
    height: 780px;
    background: var(--label-black);
    overflow: hidden;
  }
  .rule {
    position: absolute;
    left: 0;
    width: 100%;
  }
  .rule--top { top: 8px; height: 4px; background: var(--honey-gold); }
  .rule--header { top: 194px; height: 11px; background: linear-gradient(90deg, var(--band-orange-dark), var(--honey-orange), var(--band-orange-dark)); }
  .rule--footer { top: 717px; height: 5px; background: var(--honey-gold); }

  .brand {
    position: absolute;
    top: 12px;
    left: 0;
    width: 100%;
    height: 182px;
    display: flex;
    align-items: center;
    justify-content: center;
    gap: 14px;
  }
  .brand__dot {
    width: 22px;
    height: 22px;
    border-radius: 50%;
    background: var(--honey-gold);
  }
  .brand__name {
    font-family: "Montserrat", sans-serif;
    font-weight: 800;
    font-size: 30px;
    line-height: 1;
    letter-spacing: 2px;
    color: var(--white);
    text-transform: uppercase;
  }

  .floral-panel {
    position: absolute;
    top: 205px;
    left: 0;
    width: 100%;
    height: 333px;
    background: radial-gradient(ellipse at center, var(--paper) 0%, var(--paper) 45%, var(--floral-grey) 100%);
  }
  .title {
    position: absolute;
    top: 205px;
    left: 0;
    width: 100%;
    height: 333px;
    text-align: center;
    font-family: "Oswald", sans-serif;
    font-weight: 700;
    color: var(--ink);
    text-transform: uppercase;
  }
  .title__kind {
    display: block;
    margin-top: 74px;
    font-size: 64px;
    line-height: 1;
    letter-spacing: 1px;
    text-shadow: 3px 2px 0 var(--honey-gold);
  }
  .title__product {
    display: block;
    margin-top: 20px;
    font-size: 150px;
    line-height: 1;
    letter-spacing: 8px;
    text-shadow: 5px 3px 0 var(--honey-gold);
  }

  .claim-band {
    position: absolute;
    top: 538px;
    left: 0;
    width: 100%;
    height: 51px;
    background: linear-gradient(90deg, var(--band-orange-dark), var(--honey-orange) 50%, var(--band-orange-dark));
    display: flex;
    align-items: center;
    justify-content: center;
  }
  .claim-band__text {
    font-family: "Montserrat", sans-serif;
    font-weight: 800;
    font-size: 27px;
    line-height: 1;
    color: var(--ink);
    text-transform: uppercase;
  }
  .origin {
    position: absolute;
    top: 610px;
    left: 0;
    width: 100%;
    height: 54px;
    text-align: center;
    font-family: "Montserrat", sans-serif;
    font-weight: 800;
    font-size: 48px;
    line-height: 54px;
    letter-spacing: 2px;
    color: var(--white);
    text-transform: uppercase;
  }
  .net-weight {
    position: absolute;
    left: 234px;
    top: 694px;
    width: 52px;
    height: 52px;
    border-radius: 50%;
    background: var(--honey-gold);
    display: flex;
    align-items: center;
    justify-content: center;
    font-family: "Montserrat", sans-serif;
    font-weight: 700;
    font-size: 18px;
    line-height: 1;
    color: var(--ink);
  }
</style>
</head>
<body>
<main class="canvas">
  <section class="label">
    <div class="rule rule--top"></div>
    <header class="brand">
      <span class="brand__dot"></span>
      <span class="brand__name">Palmetto Grove</span>
    </header>
    <div class="rule rule--header"></div>

    <div class="floral-panel" role="img" aria-label="Black and white line illustration of wildflowers behind the product name"></div>
    <h1 class="title">
      <span class="title__kind">Wildflower</span>
      <span class="title__product">Honey</span>
    </h1>

    <div class="claim-band"><span class="claim-band__text">100% Pure &amp; Unfiltered</span></div>
    <p class="origin">Florida</p>
    <div class="rule rule--footer"></div>
    <div class="net-weight">12oz</div>
  </section>
</main>
</body>
</html>
```